KVT Business Cards

We require business cards for our business. We would like a matte black back to the card, with our logo centred in the middle. The front side of the card is open to design.

Target Market(s)

Clients looking for legal services (professional)

Industry/Entity Type

Legal

Contact Information for Business Card

Boris Telemark
Partner
Mobile: 0438 715 642
Email: boris@kvtlaw.co
Website: www.kvtlaw.co
Level 3, 118 Wexbury Street
Sydney NSW 2000

Font styles to use
Other font styles liked:
• Avenir

Colors
f04a50
ffffff
1b1b1b

Requirements
Must have
• Black back with logo included in the centre of the card.
• Our font is Avenir.

```html
<!DOCTYPE html>
<html lang="en">
<head>
<meta charset="utf-8">
<title>KVT Legal – Business Cards</title>
<link rel="stylesheet" href="https://fonts.googleapis.com/css2?family=Nunito+Sans:wght@400;700;800&display=swap">
<style>
  :root {
    --coral: #f04a50;
    --crimson: #c21e45;
    --ink: #1b1b1b;
    --deep: #0c0c0c;
    --paper: #ffffff;
    --text-dark: #111111;
    --font: "Nunito Sans", "Avenir", Arial, sans-serif;
  }
  html, body {
    margin: 0;
    width: 1200px;
    height: 1200px;
    overflow: hidden;
    background: var(--paper);
    font-family: var(--font);
  }
  .canvas {
    position: relative;
    width: 1200px;
    height: 1200px;
  }
  .card {
    position: absolute;
    left: 232px;
    width: 720px;
    height: 360px;
    background: var(--ink);
    box-shadow: 50px 80px 60px rgba(0, 0, 0, 0.72);
    overflow: hidden;
  }

  /* Back of card: black with centred brand */
  .card-back {
    top: 138px;
    border-top: 4px solid var(--coral);
    border-bottom: 3px solid var(--coral);
    box-sizing: border-box;
  }
  .brand-mark {
    position: absolute;
    background: var(--crimson);
  }
  .brand-name {
    position: absolute;
    margin: 0;
    font-weight: 800;
    color: var(--crimson);
    line-height: 1;
    letter-spacing: 2px;
    white-space: nowrap;
  }
  .card-back .brand-mark {
    left: 80px;
    top: 105px;
    width: 140px;
    height: 140px;
  }
  .card-back .brand-name {
    left: 330px;
    top: 112px;
    font-size: 120px;
  }

  /* Front of card: contact details */
  .card-front {
    top: 718px;
    background: var(--deep);
  }
  .brand-panel {
    position: absolute;
    left: 376px;
    top: 0;
    right: 0;
    bottom: 0;
    background: var(--ink);
  }
  .card-front .brand-mark {
    left: 490px;
    top: 50px;
    width: 130px;
    height: 130px;
  }
  .card-front .brand-name {
    left: 478px;
    top: 226px;
    font-size: 76px;
  }
  .info-block {
    position: absolute;
    left: 0;
    background: var(--coral);
    border-radius: 0 6px 6px 0;
    box-shadow: 6px 6px 14px rgba(0, 0, 0, 0.6);
    color: var(--text-dark);
    font-size: 22px;
    line-height: 28px;
    letter-spacing: 0.5px;
    box-sizing: border-box;
    padding-left: 35px;
    margin: 0;
    font-style: normal;
  }
  .info-title {
    top: 0;
    width: 376px;
    height: 94px;
    padding-top: 32px;
    display: flex;
    gap: 28px;
  }
  .info-contact {
    top: 104px;
    width: 344px;
    height: 120px;
    padding-top: 16px;
  }
  .info-address {
    top: 240px;
    width: 334px;
    height: 120px;
    padding-top: 10px;
    padding-left: 33px;
    border-radius: 0 6px 0 0;
  }
  .info-block p { margin: 0; }
</style>
</head>
<body>
<main class="canvas">

  <section class="card card-back" aria-label="Card back">
    <span class="brand-mark"></span>
    <h1 class="brand-name">KVT</h1>
  </section>

  <section class="card card-front" aria-label="Card front">
    <div class="brand-panel"></div>

    <div class="info-block info-title">
      <span class="role">Partner</span>
      <span>-</span>
      <span class="person">Boris Telemark</span>
    </div>

    <div class="info-block info-contact">
      <p>Mobile: 0438 715 642</p>
      <p>Email: boris@kvtlaw.co</p>
      <p>Website: www.kvtlaw.co</p>
    </div>

    <address class="info-block info-address">
      <p>Level 3, 118 Wexbury</p>
      <p>Street</p>
      <p>Sydney NSW 2000</p>
    </address>

    <span class="brand-mark"></span>
    <span class="brand-name">KVT</span>
  </section>

</main>
</body>
</html>
```